Chicago Property Management Flyer

We need a brochure/flyer to market our property management services to Chicago property owners. I believe that my preference is single page, double sided, but a bi-fold or tri-fold format may also work. I have provided our logo, and some example images in case that is helpful. Refer to our website at http://www.velmorehq.net/ for more info.

Industry/Entity Type

Property Management

Font styles to use
Sans Serif

```html
<!DOCTYPE html>
<html lang="en">
<head>
<meta charset="utf-8">
<title>Property Management Brochure – Inside Spread</title>
<link rel="stylesheet" href="https://fonts.googleapis.com/css2?family=Sorts+Mill+Goudy&display=swap">
<style>
  :root {
    --page-bg: #ffffff;
    --navy-deep: #0d2a7e;
    --royal: #1d4fb4;
    --royal-mid: #2a5cc0;
    --sky: #8fb4e2;
    --mist: #dfe8ee;
    --teal-ink: #1f4c5a;
    --teal-body: #4a7d88;
    --white-ink: #f2f5fb;
    --navy-ink: #3a4a80;
    --photo-light: #a9b6c2;
    --photo-dark: #5f6f80;
  }
  * { margin: 0; padding: 0; box-sizing: border-box; }
  html, body {
    width: 1200px; height: 900px; overflow: hidden;
    background: var(--page-bg);
    font-family: "Sorts Mill Goudy", Georgia, serif;
  }
  .spread {
    position: absolute; left: 32px; top: 68px;
    width: 1125px; height: 744px;
    box-shadow: 6px 8px 14px rgba(0,0,0,0.35);
    overflow: hidden;
  }
  .skyline {
    position: absolute; left: 0; top: 0; width: 1125px; height: 224px;
    background: linear-gradient(180deg, var(--photo-light) 0%, var(--photo-dark) 100%);
  }
  .skyline::after {
    content: ""; position: absolute; inset: 0;
    background: linear-gradient(90deg, rgba(255,255,255,0) 75%, rgba(255,255,255,0.35) 100%);
  }
  .panel {
    position: absolute; top: 224px; height: 520px;
  }
  .panel--left {
    left: 0; width: 374px;
    background: linear-gradient(90deg, var(--royal) 0%, var(--navy-deep) 100%);
  }
  .panel--middle {
    left: 374px; width: 375px;
    background: linear-gradient(90deg, var(--royal-mid) 0%, var(--sky) 100%);
  }
  .panel--right {
    left: 749px; width: 376px;
    background: radial-gradient(ellipse at 35% 45%, #ffffff 0%, var(--mist) 45%, #b7cdd6 100%);
  }
  .facets { position: absolute; inset: 0; }
  .feature { position: absolute; left: 25px; width: 330px; }
  .panel--middle .feature, .panel--right .feature { left: 31px; }
  .feature h2 {
    font-weight: 400; font-size: 23.5px; line-height: 28px; letter-spacing: 0.3px;
  }
  .feature p {
    margin-top: 20px; font-size: 17px; line-height: 20.4px;
  }
  .feature--top { top: 52px; }
  .feature--bottom { top: 300px; }
  .feature--bottom p { margin-top: 16px; }
  .panel--left .feature, .panel--middle .feature--top { color: var(--white-ink); }
  .panel--middle .feature--bottom h2 { color: #c9d6ee; }
  .panel--middle .feature--bottom p { color: var(--navy-ink); }
  .panel--right .feature h2 { color: var(--teal-ink); }
  .panel--right .feature p { color: var(--teal-body); }
</style>
</head>
<body>
  <section class="spread">
    <div class="skyline" role="img" aria-label="Aerial photograph of a city skyline of high-rise towers along a lakefront"></div>

    <article class="panel panel--left">
      <div class="feature feature--top">
        <h2>Save Time and Headaches</h2>
        <p>We have a team in place to tackle<br>all aspects of property manage-<br>ment for you. Never worry about<br>leasing, tenants, maintenance,<br>regulations, etc.</p>
      </div>
      <div class="feature feature--bottom">
        <h2>Maximize Your<br>Investment Assets</h2>
        <p>Your properties are expensive<br>assets with lots of potential.&nbsp; Put<br>the right professionals in place to<br>protect, maintain, and maximize<br>their value.</p>
      </div>
    </article>

    <article class="panel panel--middle">
      <svg class="facets" width="375" height="520" viewBox="0 0 375 520" aria-hidden="true">
        <defs>
          <linearGradient id="mid-light" x1="0" y1="1" x2="1" y2="0">
            <stop offset="0" stop-color="#e9ecf4"/>
            <stop offset="1" stop-color="#b9c6e4"/>
          </linearGradient>
        </defs>
        <polygon points="0,520 375,260 375,520" fill="url(#mid-light)" opacity="0.9"/>
        <polygon points="0,520 180,380 375,520" fill="#ffffff" opacity="0.35"/>
        <polygon points="350,0 375,0 375,14" fill="#1a3c96"/>
      </svg>
      <div class="feature feature--top">
        <h2>Increase Income</h2>
        <p>With our experience and<br>market knowledge we can es-<br>tablish optimal rent prices,<br>lease apartments quickly,<br>reduce turnover, and navigate<br>complex housing agency pro-<br>cesses to ensure maximum<br>income to you.</p>
      </div>
      <div class="feature feature--bottom">
        <h2>Reduce Expenses,<br>Maximize Profits</h2>
        <p>Maximize your profits by benefit-<br>ting from our economies of scale,<br>systems and processes, specialized<br>knowledge, industry network, and<br>buying power</p>
      </div>
    </article>

    <article class="panel panel--right">
      <svg class="facets" width="376" height="520" viewBox="0 0 376 520" aria-hidden="true">
        <polygon points="80,0 376,0 376,120" fill="#ffffff" opacity="0.25"/>
        <polygon points="90,250 290,280 120,330" fill="#c9d2f4" opacity="0.55"/>
        <polygon points="230,360 376,300 376,520 260,520" fill="#8fb0b8" opacity="0.3"/>
        <polygon points="0,300 90,250 120,330 0,420" fill="#d6e6ea" opacity="0.5"/>
      </svg>
      <div class="feature feature--top">
        <h2>Stay Informed</h2>
        <p>With access to all of your property<br>information, documentation, and<br>financials through your online<br>portal of our property manage-<br>ment system you and your ac-<br>countant can stay informed as<br>needed</p>
      </div>
      <div class="feature feature--bottom">
        <h2>Grow Your<br>Investment Portfolio</h2>
        <p>With our management team fo-<br>cused on profitably managing<br>your existing properties, we can<br>then help you expand to future<br>investments</p>
      </div>
    </article>
  </section>
</body>
</html>
```